Quelto Marketing & Design needs a Wordpress website

We need a wordpress design for a new marketing and design company in Australia called 'Quelto Marketing & Design". The website needs to be responsive, modern, and attract new customers. It needs to be unique and different. We provide marketing and design solutions for small businesses from consulting, to flyer distribution to Facebook ads etc. We would like to see designs that use the Quelto logo colours. The final design should communicate professionalism, creativity & growth. It needs to stand out from the crowd.

Target Market(s)

Small Business who need a marketing freelancer to help them grow

Industry/Entity Type

Marketing

Number of Pages Required

3 page

Requirements
Must have
• Home page, services page & contact page

```html
<!DOCTYPE html>
<html lang="en">
<head>
<meta charset="utf-8">
<title>Quelto Marketing &amp; Design</title>
<link href="https://fonts.googleapis.com/css2?family=Open+Sans:wght@400;600;700;800&display=swap" rel="stylesheet">
<style>
:root{
  --pink:#e6197f;
  --pink-soft:#f06aa9;
  --ink:#2b2b2b;
  --muted:#8a8a8a;
  --line:#dcdcdc;
  --light:#f2f2f2;
  --footer:#262626;
  --footer-deep:#1b1b1b;
  --white:#ffffff;
}
*{box-sizing:border-box;margin:0;padding:0}
html,body{width:1200px;height:3636px;overflow:hidden}
body{font-family:"Open Sans",Arial,sans-serif;color:var(--ink);background:var(--white);position:relative}
.abs{position:absolute}

/* header */
.site-header{position:absolute;top:0;left:0;width:1200px;height:80px;background:var(--white);border-bottom:3px solid var(--pink)}
.brand{position:absolute;left:120px;top:14px;display:flex;align-items:center;gap:10px}
.brand-dot{width:44px;height:44px;border-radius:50%;background:var(--pink)}
.brand-name{font-size:30px;font-weight:800;color:var(--ink);line-height:1}
.brand-tag{font-size:9px;letter-spacing:2px;color:var(--pink);font-weight:600;margin-top:3px}
.social-top{position:absolute;right:120px;top:12px;display:flex;gap:6px}
.social-top span{width:18px;height:18px;border-radius:3px;background:var(--pink)}
.main-nav{position:absolute;right:120px;top:46px;display:flex;gap:22px;font-size:11px;font-weight:700;letter-spacing:.5px}
.main-nav a{color:var(--ink);text-decoration:none}
.main-nav a.active{color:var(--pink)}

/* hero */
.hero{position:absolute;top:83px;left:0;width:1200px;height:497px;background:linear-gradient(135deg,#e9e9e9 0%,#cfcfcf 45%,#bdbdbd 100%)}
.hero-caption{position:absolute;left:240px;top:180px;width:700px;background:var(--pink);padding:18px 26px;color:var(--white);font-size:27px;font-weight:700;line-height:1.25}
.hero-arrow{position:absolute;top:228px;width:34px;height:34px;border-radius:50%;background:rgba(255,255,255,.75)}
.hero-arrow svg{display:block;margin:9px auto}
.hero-arrow.prev{left:24px}.hero-arrow.next{right:24px}

/* section titles */
.section-title{position:absolute;left:0;width:1200px;text-align:center;font-size:19px;font-weight:800;letter-spacing:.5px;text-transform:uppercase}
.section-sub{position:absolute;left:0;width:1200px;text-align:center;font-size:12px;color:var(--pink)}

/* welcome */
.welcome-rule{position:absolute;left:570px;top:668px;width:60px;height:2px;background:var(--pink)}
.welcome-mock{position:absolute;left:280px;top:760px;width:640px;height:440px;background:linear-gradient(160deg,#f4f4f4 0%,#dedede 60%,#c9c9c9 100%)}

/* what we do */
.what-band{position:absolute;top:1250px;left:0;width:1200px;height:110px;background:var(--pink);color:var(--white)}
.what-band h2{text-align:center;font-size:19px;font-weight:800;margin-top:28px}
.what-band p{text-align:center;font-size:12px;margin-top:10px}
.offer-row{position:absolute;top:1360px;left:0;width:1200px;height:154px;display:flex}
.offer{position:relative;height:154px;color:var(--white);font-weight:800;text-transform:uppercase}
.offer-start{width:600px;background:linear-gradient(120deg,#f4dd3a 0%,#f6c02b 50%,#f0e6c8 100%)}
.offer-consult{width:300px;background:linear-gradient(120deg,#6b7c8f 0%,#8fa0b1 60%,#c8d0d8 100%)}
.offer-portfolio{width:300px;background:linear-gradient(120deg,#1e1e1e 0%,#3b3b3b 100%)}
.tag-dark{position:absolute;background:rgba(40,40,40,.85);padding:6px 10px;font-size:22px;line-height:1.05}
.tag-pink{position:absolute;background:var(--pink);padding:8px 12px;font-size:22px;line-height:1.05}

/* services */
.services{position:absolute;top:1560px;left:100px;width:1000px;display:flex}
.service{width:250px;text-align:center}
.service-ring{width:96px;height:96px;margin:0 auto;border-radius:50%;border:4px solid var(--pink);display:flex;align-items:center;justify-content:center}
.service h3{font-size:15px;font-weight:800;margin-top:18px;text-transform:uppercase}
.service p{font-size:11px;color:var(--muted);line-height:1.55;margin:10px auto 0;width:190px}

/* clients */
.clients{position:absolute;top:1850px;left:0;width:1200px;height:410px;background:var(--light)}
.card{position:absolute;top:100px;height:230px;background:var(--white);border:1px solid var(--line)}
.card.quote{left:140px;width:440px;padding:26px 30px}
.card.quote p{font-size:12px;font-style:italic;color:#555;line-height:1.65}
.quote-author{display:flex;align-items:center;gap:10px;margin-top:26px;font-size:10px;font-weight:700;color:var(--muted);text-transform:uppercase}
.avatar{width:36px;height:36px;border-radius:50%;background:#b8b8b8}
.card.logos{left:620px;width:440px;padding:30px;display:grid;grid-template-columns:1fr 1fr 1fr;gap:24px 14px;align-content:center}
.client-name{display:flex;align-items:center;justify-content:center;gap:6px;font-size:13px;font-weight:600;color:#9a9a9a}
.client-name i{width:12px;height:12px;border-radius:50%;background:#c4c4c4;display:block}
.dots{position:absolute;top:346px;display:flex;gap:5px}
.dots span{width:7px;height:7px;border-radius:50%;background:#c8c8c8}
.dots span.on{background:#555}

/* strip */
.work-strip{position:absolute;top:2272px;left:0;width:1200px;height:256px;display:flex}
.work-strip div{height:256px}

/* contact */
.contact-mark{position:absolute;left:140px;top:2660px;width:120px;height:120px;border-radius:50%;background:var(--pink)}
.contact-info{position:absolute;left:300px;top:2660px;font-size:13px;line-height:1.6}
.contact-info h3{font-size:14px;font-weight:800;text-transform:uppercase;margin-bottom:10px}
.contact-info .gap{margin-top:12px}
.contact-info a{color:var(--pink);text-decoration:none}
.contact-social{display:flex;gap:6px;margin-top:12px}
.contact-social span{width:20px;height:20px;border-radius:3px;background:var(--pink)}
.contact-form{position:absolute;left:780px;top:2650px;width:280px}
.field{height:34px;border:1px solid var(--line);margin-bottom:10px;font-size:12px;color:#aaa;padding:9px 10px}
.field.area{height:60px}
.btn{display:inline-block;background:var(--pink);color:var(--white);font-size:11px;font-weight:700;padding:9px 16px;text-transform:uppercase}

/* map */
.map{position:absolute;top:2860px;left:0;width:1200px;height:300px;background:linear-gradient(180deg,#ececec 0%,#dcdcdc 100%)}
.map-pin{position:absolute;left:582px;top:2930px}

/* footer */
.site-footer{position:absolute;top:3160px;left:0;width:1200px;height:476px;background:var(--footer);color:#bdbdbd}
.f-col{position:absolute;top:44px;font-size:11px;line-height:2}
.f-col h4{color:var(--white);font-size:12px;font-weight:700;text-transform:uppercase;margin-bottom:10px}
.f-col ul{list-style:none}
.f-col li::before{content:"› ";color:var(--pink)}
.f-input{width:240px;height:30px;background:#3a3a3a;margin:6px 0 10px}
.f-social{display:flex;gap:6px}
.f-social span{width:20px;height:20px;border-radius:50%;background:#555}
.footer-bar{position:absolute;bottom:0;left:0;width:1200px;height:46px;background:var(--footer-deep);font-size:10px;color:#888;padding:16px 140px}
</style>
</head>
<body>

<header class="site-header">
  <div class="brand">
    <div class="brand-dot"></div>
    <div>
      <div class="brand-name">Quelto</div>
      <div class="brand-tag">MARKETING &amp; DESIGN</div>
    </div>
  </div>
  <div class="social-top" aria-label="Social links"><span></span><span></span><span></span><span></span></div>
  <nav class="main-nav">
    <a class="active">HOME</a><a>ABOUT US</a><a>PORTFOLIO</a><a>SERVICES</a><a>CONTACT</a>
  </nav>
</header>

<section class="hero" role="img" aria-label="Photo of a whiteboard covered with hand-drawn marketing sketches">
  <div class="hero-caption">Quelto Marketing and Design is<br>a boutique marketing and design service</div>
  <div class="hero-arrow prev"><svg width="16" height="16" viewBox="0 0 16 16"><path d="M10 2 4 8l6 6" fill="none" stroke="#555" stroke-width="2"/></svg></div>
  <div class="hero-arrow next"><svg width="16" height="16" viewBox="0 0 16 16"><path d="M6 2l6 6-6 6" fill="none" stroke="#555" stroke-width="2"/></svg></div>
</section>

<h2 class="section-title" style="top:636px">Welcome to Quelto Marketing &amp; Design</h2>
<div class="welcome-rule"></div>
<p class="section-sub" style="top:688px">Quelto Marketing and Design is a boutique marketing and design service in Australia. We are here to help you grow.<br>Good ideas, clear design and real results for small business.</p>
<div class="welcome-mock" role="img" aria-label="Laptop, tablet and phone showing website and print work"></div>

<section class="what-band">
  <h2>WHAT WE DO</h2>
  <p>In each of the three rounds a package and a consult option</p>
</section>

<div class="offer-row">
  <div class="offer offer-start" role="img" aria-label="Row of hanging light bulbs">
    <div class="tag-dark" style="left:150px;top:12px">Just<br>starting up?</div>
    <div class="tag-pink" style="left:200px;top:90px">Need a marketing<br>boost or revamp?</div>
  </div>
  <div class="offer offer-consult" role="img" aria-label="Business meeting at a table">
    <div class="tag-dark" style="left:10px;top:20px">Marketing<br>consult<br>or advise</div>
  </div>
  <div class="offer offer-portfolio" role="img" aria-label="Dark portfolio image">
    <div style="position:absolute;left:40px;top:58px;font-size:24px;display:flex;align-items:center;gap:12px">Portfolio
      <svg width="26" height="20" viewBox="0 0 26 20"><path d="M0 10h22M14 2l8 8-8 8" fill="none" stroke="#fff" stroke-width="3"/></svg>
    </div>
  </div>
</div>

<section class="services">
  <div class="service">
    <div class="service-ring"><svg width="44" height="44" viewBox="0 0 44 44"><path d="M8 36 30 14l4 4-22 22H8z" fill="#2b2b2b"/><path d="M32 6l6 6-3 3-6-6z" fill="#e6197f"/></svg></div>
    <h3>Logo Design</h3>
    <p>Clean marks that tell your story, built to work on web, print and signs alike.</p>
  </div>
  <div class="service">
    <div class="service-ring"><svg width="44" height="44" viewBox="0 0 44 44"><path d="M4 24l10-10 8 6 8-6 10 10-12 10-6-4-6 4z" fill="#f2b233"/></svg></div>
    <h3>Corporate Identity</h3>
    <p>Cards, letterheads and brand kits that keep every touch point looking sharp.</p>
  </div>
  <div class="service">
    <div class="service-ring"><svg width="44" height="44" viewBox="0 0 44 44"><rect x="10" y="6" width="22" height="30" fill="#f2b233"/><rect x="14" y="10" width="22" height="30" fill="#fff" stroke="#2b2b2b" stroke-width="2"/></svg></div>
    <h3>Flyers</h3>
    <p>Eye-catching flyers designed, printed and handed out across your local area.</p>
  </div>
  <div class="service">
    <div class="service-ring"><svg width="44" height="44" viewBox="0 0 44 44"><rect x="6" y="14" width="32" height="22" rx="3" fill="#2b2b2b"/><rect x="16" y="8" width="12" height="6" fill="none" stroke="#2b2b2b" stroke-width="3"/><rect x="18" y="22" width="8" height="6" fill="#e6197f"/></svg></div>
    <h3>Consulting</h3>
    <p>Plain advice on where to spend, what to say and how to reach more customers.</p>
  </div>
</section>

<section class="clients">
  <h2 class="section-title" style="top:30px">Our Clients</h2>
  <p class="section-sub" style="top:62px">Read what our clients say, and see the brands we have helped grow</p>
  <div class="card quote">
    <p>"Quelto turned our scattered ideas into a clear plan. Our new flyers and ads brought in more calls in one month than we had all year. The team listens, explains every step and always delivers on time. We could not be happier with the work and the results."</p>
    <div class="quote-author"><div class="avatar"></div>Dana Whitfield</div>
  </div>
  <div class="dots" style="left:340px"><span class="on"></span><span></span><span></span><span></span></div>
  <div class="card logos">
    <div class="client-name"><i></i>Harbor Co</div>
    <div class="client-name"><i></i>Lumen</div>
    <div class="client-name"><i></i>Fieldstone</div>
    <div class="client-name"><i></i>Harbor Co</div>
    <div class="client-name"><i></i>Brightway</div>
    <div class="client-name"><i></i>Arcwell</div>
  </div>
  <div class="dots" style="left:820px"><span class="on"></span><span></span><span></span><span></span></div>
</section>

<section class="work-strip">
  <div style="width:200px;background:linear-gradient(135deg,#f3c74a,#e48a2d)" role="img" aria-label="Book cover design"></div>
  <div style="width:300px;background:linear-gradient(135deg,#3f8fb8,#6fb7d6)" role="img" aria-label="Website design on screen"></div>
  <div style="width:180px;background:linear-gradient(135deg,#8e1f3a,#c64b5d)" role="img" aria-label="Wine bar menu designs"></div>
  <div style="width:260px;background:linear-gradient(135deg,#d9c7a8,#a8875c)" role="img" aria-label="Poster design"></div>
  <div style="width:260px;background:linear-gradient(135deg,#7ab648,#3f8b3a)" role="img" aria-label="Business card designs"></div>
</section>

<h2 class="section-title" style="top:2566px">Contact Us</h2>
<p class="section-sub" style="top:2600px">We'd love to hear from you, drop us a line about your next project</p>
<div class="contact-mark" aria-label="Quelto mark"></div>
<div class="contact-info">
  <h3>Quelto Marketing &amp; Design</h3>
  <div>Address Line 1,<br>Address Line 2</div>
  <div class="gap">Phone: (02) 5550 1847<br>Email: <a>http://quelto.studio</a></div>
  <div class="contact-social"><span></span><span></span><span></span><span></span></div>
</div>
<div class="contact-form">
  <div class="field">Name</div>
  <div class="field">Email</div>
  <div class="field">Phone</div>
  <div class="field area">Message</div>
  <div class="btn">Submit</div>
</div>

<div class="map" role="img" aria-label="Street map showing the studio location"></div>
<svg class="map-pin" width="36" height="50" viewBox="0 0 36 50"><path d="M18 0C8 0 0 8 0 18c0 13 18 32 18 32s18-19 18-32C36 8 28 0 18 0z" fill="#e6197f"/><circle cx="18" cy="18" r="7" fill="#fff"/></svg>

<footer class="site-footer">
  <div class="f-col" style="left:140px">
    <h4>Featured Links</h4>
    <ul><li>Our services</li><li>Small business plans</li><li>Flyer distribution</li><li>Social media ads</li><li>Brand and logo design</li></ul>
  </div>
  <div class="f-col" style="left:330px;top:76px">
    <ul><li>Portfolio gallery</li><li>Client stories</li><li>Latest news</li><li>Pricing packages</li><li>Contact our team</li></ul>
  </div>
  <div class="f-col" style="left:600px">
    <h4>Contact Info</h4>
    <div>Quelto Marketing &amp; Design</div>
    <div>Address Line 1, Line 2</div>
    <div>Phone: (02) 5550 1847</div>
    <div>Email: hello@quelto.studio</div>
  </div>
  <div class="f-col" style="left:820px">
    <h4>Join Our Mailing List</h4>
    <div class="f-input"></div>
    <div class="btn" style="font-size:10px;padding:6px 12px">Subscribe</div>
    <h4 style="margin-top:16px">Follow Us</h4>
    <div class="f-social"><span></span><span></span><span></span><span></span><span></span></div>
  </div>
  <div class="footer-bar">© 2015 All Rights Reserved</div>
</footer>

</body>
</html>
```